Design a business card
Business name: Kestrel Yield Consulting
Improving Business Profitibility

- An Overview of the Business & Service:

Improving business profitability

- The Target Market: Small to medium-sized business

- Design Specifics:
White card, blue ink, moon eclipse

No Logo

Target Market(s)

Small to medium-sized business

Font styles to use
Sans Serif

```html
<!DOCTYPE html>
<html lang="en">
<head>
<meta charset="utf-8">
<title>Kestrel Yield Consulting — Business Card</title>
<link rel="stylesheet" href="https://fonts.googleapis.com/css2?family=Montserrat:wght@400;700&display=swap">
<style>
  :root {
    --ink: #1c1a57;
    --paper: #ffffff;
    --backdrop: #e4e4e7;
    --card-shadow: rgba(20, 20, 40, 0.18);
  }
  * { box-sizing: border-box; margin: 0; padding: 0; }
  html, body { width: 1200px; height: 800px; overflow: hidden; }
  body {
    background: var(--backdrop);
    font-family: "Montserrat", Arial, sans-serif;
    position: relative;
  }
  .card {
    position: absolute;
    top: 252px;
    width: 520px;
    height: 297px;
    box-shadow: 0 10px 28px var(--card-shadow);
  }
  .card--front { left: 50px; background: var(--paper); color: var(--ink); }
  .card--back  { left: 630px; background: var(--ink); color: var(--paper); }

  .brand { position: absolute; }
  .brand__name {
    font-weight: 700;
    font-size: 25px;
    text-transform: uppercase;
    white-space: nowrap;
    line-height: 1;
  }
  .brand__promise {
    font-weight: 400;
    font-size: 13px;
    white-space: nowrap;
    margin-top: 12px;
  }
  .card--front .brand { left: 36px; top: 40px; }
  .card--back .brand { left: 50%; top: 50%; transform: translate(-50%, -50%); text-align: center; }

  .contact { position: absolute; left: 36px; top: 130px; }
  .contact__name {
    font-weight: 700;
    font-size: 15px;
    text-transform: uppercase;
    letter-spacing: 0.3px;
  }
  .contact__role { font-size: 13px; margin-top: 2px; margin-bottom: 12px; }
  .contact__list { list-style: none; }
  .contact__item {
    display: flex;
    align-items: center;
    gap: 8px;
    font-size: 11.5px;
    line-height: 1.55;
  }
  .contact__icon { width: 11px; height: 11px; flex: none; fill: var(--ink); }
</style>
</head>
<body>

  <section class="card card--front" aria-label="Card front">
    <div class="brand">
      <div class="brand__name">Kestrel Yield Consulting</div>
      <div class="brand__promise">Improving business profitability</div>
    </div>
    <div class="contact">
      <div class="contact__name">Desmond R Hale</div>
      <div class="contact__role">Business consultant</div>
      <ul class="contact__list">
        <li class="contact__item">
          <svg class="contact__icon" viewBox="0 0 24 24" aria-hidden="true"><path d="M6.6 10.8a15 15 0 0 0 6.6 6.6l2.2-2.2c.3-.3.7-.4 1-.2 1.1.4 2.3.6 3.6.6.6 0 1 .4 1 1V20c0 .6-.4 1-1 1A17 17 0 0 1 3 4c0-.6.4-1 1-1h3.5c.6 0 1 .4 1 1 0 1.3.2 2.5.6 3.6.1.3 0 .7-.2 1z"/></svg>
          555-014-2278
        </li>
        <li class="contact__item">
          <svg class="contact__icon" viewBox="0 0 24 24" aria-hidden="true"><path d="M2 5h20v14H2z M3.5 6.5 12 13l8.5-6.5" fill="none" stroke="#1c1a57" stroke-width="2"/><path d="M2 5h20v2l-10 7L2 7z"/></svg>
          info@kestrelyieldconsulting.com
        </li>
        <li class="contact__item">
          <svg class="contact__icon" viewBox="0 0 24 24" aria-hidden="true"><circle cx="12" cy="12" r="10" fill="none" stroke="#1c1a57" stroke-width="2"/><path d="M2 12h20M12 2c3 3 3 17 0 20M12 2c-3 3-3 17 0 20" fill="none" stroke="#1c1a57" stroke-width="1.6"/></svg>
          kestrelyieldconsulting.com
        </li>
      </ul>
    </div>
  </section>

  <section class="card card--back" aria-label="Card back">
    <div class="brand">
      <div class="brand__name">Kestrel Yield Consulting</div>
      <div class="brand__promise">Improving business profitability</div>
    </div>
  </section>

</body>
</html>
```